Hi,

I have an event coming up for my nightclub Crimson At Wexley called Tempo Saturdays with the radio station Tempo FM,

I need a poster done up promoting the event, the date of the event is Friday the 25th of October at Crimson at Wexley and also its featuring Tempo's own DJ Rivolt.

You can add drink specials available on the night,

Open from 9pm till late

Requirements
Must have

```html
<!DOCTYPE html>
<html lang="en">
<head>
<meta charset="utf-8">
<title>Tempo Saturdays at Crimson at Wexley</title>
<link rel="stylesheet" href="https://fonts.googleapis.com/css2?family=Oswald:wght@500;600&family=Cinzel:wght@600&family=Open+Sans:wght@400;700&family=Raleway:wght@300&display=swap">
<style>
  :root {
    --night: #0b0609;
    --deep-red: #3a0a12;
    --club-red: #b3122a;
    --hot-red: #e8283c;
    --gold-light: #f7e2a0;
    --gold: #c9a24a;
    --gold-dark: #8a6a24;
    --violet: #b33cf0;
    --violet-deep: #7a1fb0;
    --tempo-orange: #ff8a1a;
    --white: #ffffff;
    --silver: #d9d9de;
    --band: rgba(40, 10, 16, 0.78);
    --footer: #000000;
  }
  html, body {
    margin: 0;
    padding: 0;
    overflow: hidden;
    background: var(--night);
  }
  .poster {
    position: relative;
    width: 848px;
    height: 1200px;
    overflow: hidden;
    background:
      radial-gradient(ellipse 70% 45% at 62% 48%, rgba(232, 40, 60, 0.55), transparent 70%),
      radial-gradient(ellipse 90% 60% at 50% 55%, var(--deep-red), transparent 80%),
      linear-gradient(180deg, #120508 0%, #1e060c 40%, #2a0a12 70%, #12050a 100%);
    font-family: "Open Sans", Arial, sans-serif;
    color: var(--white);
  }
  .dance-floor {
    position: absolute;
    left: 0;
    top: 360px;
    width: 848px;
    height: 520px;
    background:
      radial-gradient(ellipse 60% 50% at 75% 40%, rgba(255, 50, 70, 0.45), transparent 70%),
      linear-gradient(160deg, rgba(180, 20, 40, 0.25), rgba(90, 10, 25, 0.35));
  }
  .event-date {
    position: absolute;
    top: 40px;
    left: 0;
    width: 100%;
    margin: 0;
    text-align: center;
    font-family: "Oswald", Impact, sans-serif;
    font-weight: 600;
    font-size: 92px;
    line-height: 1;
    letter-spacing: 1px;
    background: linear-gradient(180deg, var(--gold-light) 0%, var(--gold) 55%, var(--gold-dark) 100%);
    -webkit-background-clip: text;
    background-clip: text;
    color: transparent;
  }
  .event-date sup {
    font-size: 0.5em;
    vertical-align: 0.75em;
  }
  .venue-rule {
    position: absolute;
    top: 197px;
    left: 194px;
    width: 460px;
    height: 5px;
    background: var(--violet);
    box-shadow: 0 0 10px var(--violet);
  }
  .venue-name {
    position: absolute;
    top: 224px;
    left: 0;
    width: 100%;
    margin: 0;
    text-align: center;
    font-family: "Cinzel", Georgia, serif;
    font-weight: 600;
    font-size: 40px;
    letter-spacing: 4px;
    color: var(--white);
  }
  .venue-ornament {
    position: absolute;
    top: 303px;
    left: 204px;
    width: 440px;
    height: 130px;
    background: radial-gradient(ellipse 50% 50% at 50% 40%, var(--violet), var(--violet-deep) 60%, transparent 100%);
    opacity: 0.85;
  }
  .event-title {
    position: absolute;
    top: 430px;
    left: 0;
    width: 100%;
    margin: 0;
    text-align: center;
    font-family: "Oswald", Impact, sans-serif;
    font-weight: 600;
    color: var(--tempo-orange);
    line-height: 0.95;
  }
  .event-title .title-main {
    display: block;
    font-size: 172px;
    letter-spacing: 2px;
  }
  .event-title .title-day {
    display: block;
    font-size: 108px;
    letter-spacing: 6px;
  }
  .crowd-band {
    position: absolute;
    top: 836px;
    left: 0;
    width: 848px;
    height: 176px;
    background: linear-gradient(180deg, rgba(110, 20, 35, 0.7), var(--band));
  }
  .featuring {
    position: absolute;
    top: 842px;
    left: 0;
    width: 100%;
    margin: 0;
    text-align: center;
    font-size: 38px;
    font-weight: 400;
    color: var(--white);
  }
  .headliner {
    position: absolute;
    top: 900px;
    left: 0;
    width: 100%;
    margin: 0;
    text-align: center;
    font-family: "Raleway", Arial, sans-serif;
    font-weight: 300;
    font-size: 76px;
    letter-spacing: 5px;
    color: var(--silver);
  }
  .footer {
    position: absolute;
    top: 1012px;
    left: 0;
    width: 848px;
    height: 188px;
    background: var(--footer);
  }
  .opening-hours {
    position: absolute;
    top: 1026px;
    left: 0;
    width: 100%;
    margin: 0;
    text-align: center;
    font-weight: 700;
    font-size: 42px;
    color: var(--white);
  }
  .website {
    position: absolute;
    top: 1118px;
    left: 0;
    width: 100%;
    margin: 0;
    text-align: center;
    font-size: 20px;
    color: var(--white);
  }
</style>
</head>
<body>
  <main class="poster">
    <div class="dance-floor" role="img" aria-label="Glowing red dance floor tiles with light flares and sound waves"></div>

    <h2 class="event-date">25<sup>TH</sup> OCT. FRIDAY</h2>

    <div class="venue-rule"></div>
    <p class="venue-name">CRIMSON AT WEXLEY</p>
    <div class="venue-ornament" role="img" aria-label="Violet baroque flourish ornament"></div>

    <h1 class="event-title">
      <span class="title-main">TEMPO</span>
      <span class="title-day">SATURDAYS</span>
    </h1>

    <div class="crowd-band" role="img" aria-label="Silhouetted crowd with raised hands on a dark red band"></div>
    <p class="featuring">Featuring Tempo’s Own</p>
    <p class="headliner">DJ RIVOLT</p>

    <footer class="footer"></footer>
    <p class="opening-hours">OPEN 9PM TILL LATE</p>
    <p class="website">www.crimsonatwexley.com</p>
  </main>
</body>
</html>
```